Wedding design templates - fresh

We require 3 different wedding designs. I have attached the watercolour images for the graphic designer to use on each template. I want to be able to easily change the name and location of the invitation when needed and be able to freely use whatever font is used, so that the invite becomes our template. I want something fresh with a modern layout but on a white background. The use of coloured fonts are okay to suit the images provided. The size of the card stock is A5 (half of an A4) please consider bleeds etc for printing.

Target Market(s)

Bridal market - young couples

Industry/Entity Type

Wedding

Font styles to use
Serif
Sans Serif
Script

Requirements
Must have
• Be able to use fonts and change details easily. common colours that can easily fit in with a brides colour scheme. must have all details for wedding invites ie church name address etc can be any church or reception place in sydney
Nice to have
• i have uploaded some example images as to style i am looking for.
• I want to be able to run a theme with these images eg. rsvp cards, place cards etc

```html
<!DOCTYPE html>
<html lang="en">
<head>
<meta charset="utf-8">
<title>Elise &amp; Tom – Wedding Invitation</title>
<link href="https://fonts.googleapis.com/css2?family=Josefin+Sans:wght@300;400&family=Parisienne&display=swap" rel="stylesheet">
<style>
  :root {
    --paper: #ffffff;
    --ink: #4f4a4c;
    --plum: #7b3b52;
    --blush: #f2c9d0;
    --blush-deep: #e7a9b6;
    --sage: #a9bf98;
    --cream: #f1eed8;
  }
  html, body {
    margin: 0;
    padding: 0;
    overflow: hidden;
    background: var(--paper);
  }
  .invitation {
    position: relative;
    width: 1200px;
    height: 848px;
    background: var(--paper);
    overflow: hidden;
    font-family: "Josefin Sans", "Helvetica Neue", Arial, sans-serif;
    color: var(--ink);
  }
  .floral-art {
    position: absolute;
    left: 0;
    top: 0;
    width: 560px;
    height: 848px;
  }
  .details {
    position: absolute;
    right: 38px;
    top: 0;
    width: 760px;
    height: 848px;
    text-align: right;
  }
  .line {
    position: absolute;
    right: 0;
    margin: 0;
    white-space: nowrap;
    font-weight: 300;
    font-variant: small-caps;
    letter-spacing: 1.5px;
    line-height: 1;
  }
  .line--small { font-size: 22px; }
  .line--body { font-size: 27px; }
  .script {
    position: absolute;
    right: 0;
    margin: 0;
    white-space: nowrap;
    font-family: "Parisienne", "Brush Script MT", cursive;
    font-weight: 400;
    color: var(--plum);
    line-height: 1;
  }
  .script--names { font-size: 92px; top: 112px; }
  .script--venue { font-size: 52px; }

  .intro { top: 66px; }
  .invite-line { top: 236px; }
  .date-day { top: 302px; }
  .date-year { top: 338px; }
  .date-time { top: 374px; }
  .ceremony-venue { top: 428px; }
  .ceremony-address { top: 502px; }
  .reception-heading { top: 546px; }
  .reception-address { top: 612px; }
  .rsvp-heading { top: 702px; }
  .rsvp-details { top: 768px; }
</style>
</head>
<body>
<main class="invitation">
  <svg class="floral-art" viewBox="0 0 560 848" role="img" aria-label="Watercolour bouquet of pale pink blossoms with sage eucalyptus leaves and cream baby's breath">
    <defs>
      <radialGradient id="bouquetWash" cx="42%" cy="50%" r="60%">
        <stop offset="0%" stop-color="#f2c9d0"/>
        <stop offset="45%" stop-color="#f6dde1"/>
        <stop offset="75%" stop-color="#eef0e2"/>
        <stop offset="100%" stop-color="#ffffff"/>
      </radialGradient>
    </defs>
    <rect width="560" height="848" fill="url(#bouquetWash)"/>
  </svg>

  <section class="details">
    <p class="line line--small intro">Together with their families</p>
    <h1 class="script script--names">Elise &amp; Tom</h1>
    <p class="line line--small invite-line">invite you to join them as they tie the knot</p>
    <p class="line line--small date-day">Saturday the Tenth of August,</p>
    <p class="line line--small date-year">two thousand fifteen</p>
    <p class="line line--small date-time">at Three O’clock in the Afternoon</p>
    <h2 class="script script--venue ceremony-venue">St Aldens Church</h2>
    <p class="line line--body ceremony-address">Meadow Lane, Ashford, AB1 2CD</p>
    <h2 class="script script--venue reception-heading">Reception to follow at</h2>
    <p class="line line--body reception-address">The Granary, 14 Millbrook Street, MB3 7QT</p>
    <h2 class="script script--venue rsvp-heading">Rsvp by</h2>
    <p class="line line--body rsvp-details">25th March at eliseandtom@mailbox.com</p>
  </section>
</main>
</body>
</html>
```